Birchford Realty Business Card

Business Card:

Somewhere on front of card, please include Broker License Number: 5839162

Website is BirchfordRealty.example

Address is:
7218 Crestover Ave E
Dunmere, OR 48271

I'll let you use creative freedom on the rest; we obviously need Name, Title, Email (@BirchfordRealty.example), Office Phone, Cell Phone.

Don't want any special die-cutting, just a standard size business card.

On the back, include a place for the date and time of an appointment to be written in pen.

Requirements
Must have
• Our logo, attached to email.

```html
<!DOCTYPE html>
<html lang="en">
<head>
<meta charset="utf-8">
<title>Birchford Realty Business Card</title>
<link rel="stylesheet" href="https://fonts.googleapis.com/css2?family=Ubuntu:wght@500;700&family=Roboto:wght@400;500&display=swap">
<style>
  :root {
    --brand-blue: #3a3aa8;
    --brand-blue-soft: #5252b8;
    --paper: #ffffff;
    --paper-grey: #e4e4e6;
    --paper-shade: #cfd0d3;
    --ink: #2a2a2a;
    --muted: #a7a8ad;
    --stage: #ececef;
  }
  * { box-sizing: border-box; margin: 0; padding: 0; }
  html, body { width: 1200px; height: 902px; overflow: hidden; }
  body {
    background: var(--stage);
    font-family: "Roboto", Arial, sans-serif;
    display: flex;
    align-items: center;
    justify-content: center;
    gap: 50px;
  }
  .card {
    position: relative;
    width: 525px;
    height: 300px;
    background: var(--paper);
    box-shadow: 0 6px 18px rgba(0,0,0,.18);
    overflow: hidden;
  }
  .brand-name {
    font-family: "Ubuntu", Arial, sans-serif;
    font-weight: 700;
    color: var(--brand-blue-soft);
    letter-spacing: -0.5px;
    white-space: nowrap;
  }

  /* Back side */
  .card-back .back-header {
    position: absolute; inset: 0 0 auto 0; height: 128px;
    background: linear-gradient(180deg, var(--paper-shade), var(--paper-grey));
    border-bottom: 3px solid var(--brand-blue);
    display: flex; align-items: center; justify-content: center;
  }
  .card-back .brand-name { font-size: 44px; }
  .appointment {
    position: absolute; left: 36px; right: 36px; top: 160px;
    color: var(--ink); font-size: 22px;
  }
  .appointment .title { margin-bottom: 14px; }
  .appointment .field { display: flex; align-items: baseline; gap: 10px; margin: 0 0 14px 18px; }
  .appointment .line { flex: 1; border-bottom: 3px dotted var(--ink); height: 1px; }

  /* Front side */
  .card-front .front-shape { position: absolute; inset: 0; }
  .front-brand {
    position: absolute; left: 120px; top: 48px;
  }
  .card-front .brand-name { font-size: 42px; }
  .license {
    margin-top: 4px; padding-top: 4px;
    border-top: 1px solid var(--muted);
    color: var(--muted); font-size: 16px; letter-spacing: 0.5px;
    width: 250px;
  }
  .person {
    position: absolute; left: 28px; bottom: 34px; color: var(--paper);
  }
  .person .name { font-family: "Ubuntu", Arial, sans-serif; font-weight: 500; font-size: 27px; }
  .person .role { font-size: 17px; margin-top: 2px; }
  .contact-list {
    position: absolute; left: 240px; top: 176px; bottom: 18px;
    border-left: 1.5px solid var(--paper);
    padding-left: 10px;
    list-style: none; color: var(--paper); font-size: 12.5px;
    display: flex; flex-direction: column; justify-content: space-between;
  }
  .contact-list li { display: flex; align-items: center; gap: 8px; white-space: nowrap; }
  .contact-list svg { width: 16px; height: 16px; flex: none; }
</style>
</head>
<body>

  <section class="card card-back" aria-label="Card back">
    <div class="back-header">
      <span class="brand-name">Birchford Realty</span>
    </div>
    <div class="appointment">
      <p class="title">Appoinments :</p>
      <p class="field"><span>Date :</span><span class="line"></span></p>
      <p class="field"><span>Time :</span><span class="line"></span></p>
    </div>
  </section>

  <section class="card card-front" aria-label="Card front">
    <svg class="front-shape" viewBox="0 0 525 300" width="525" height="300" aria-hidden="true">
      <polyline points="0,160 60,160 85,146 460,146 510,40 525,40" fill="none" stroke="#dcdde0" stroke-width="6"/>
      <polygon points="0,176 68,176 94,162 470,162 525,58 525,300 0,300" fill="var(--brand-blue)"/>
    </svg>

    <div class="front-brand">
      <div class="brand-name">Birchford Realty</div>
      <div class="license">Lic No: 5839162</div>
    </div>

    <div class="person">
      <p class="name">Dana Whitlock</p>
      <p class="role">CEO</p>
    </div>

    <ul class="contact-list">
      <li>
        <svg viewBox="0 0 16 16"><rect width="16" height="16" rx="2" fill="#fff"/><rect x="4" y="5" width="8" height="7" rx="1" fill="var(--brand-blue)"/><rect x="3" y="3" width="10" height="2.5" rx="1" fill="var(--brand-blue)"/></svg>
        <span>045-3870-5512</span>
      </li>
      <li>
        <svg viewBox="0 0 16 16"><rect width="16" height="16" rx="2" fill="#fff"/><path d="M5 3.5l2 2-1.2 1.3a6 6 0 003.4 3.4L10.5 9l2 2-1.3 1.5C7 12.5 3.5 9 3.5 4.8z" fill="var(--brand-blue)"/></svg>
        <span>046-6143-2079</span>
      </li>
      <li>
        <svg viewBox="0 0 16 16"><rect width="16" height="16" rx="2" fill="#fff"/><rect x="3" y="4.5" width="10" height="7" fill="var(--brand-blue)"/><path d="M3 4.5l5 4 5-4" fill="none" stroke="#fff" stroke-width="1"/></svg>
        <span>dana@BirchfordRealty.example</span>
      </li>
      <li>
        <svg viewBox="0 0 16 16"><rect width="16" height="16" rx="2" fill="#fff"/><circle cx="8" cy="8" r="4.5" fill="none" stroke="var(--brand-blue)" stroke-width="1.3"/><path d="M3.5 8h9M8 3.5c-2 2.5-2 6.5 0 9M8 3.5c2 2.5 2 6.5 0 9" fill="none" stroke="var(--brand-blue)" stroke-width="1"/></svg>
        <span>www.BirchfordRealty.example</span>
      </li>
      <li>
        <svg viewBox="0 0 16 16"><rect width="16" height="16" rx="2" fill="#fff"/><path d="M8 13s-3.8-4-3.8-6.5a3.8 3.8 0 017.6 0C11.8 9 8 13 8 13z" fill="var(--brand-blue)"/><circle cx="8" cy="6.5" r="1.3" fill="#fff"/></svg>
        <span>7218 Crestover Ave E, Dunmere, OR 48271</span>
      </li>
    </ul>
  </section>

</body>
</html>
```